I am preparing a presentation for my project " Harbor Youth Retreat"
I need to help me designing and making it more professional and also ready to be printed
I just half way of my presentation so have a look and give me different options.
You will find the draft presentation that you can work on and give me some more ideas
You can also add some work art.
I need it to be printable
I want you to build the presentation on the second powerpoint " Abu Dhabi Coral Lodge"

It will be presented to an investor to be my partner in establishing this company

```html
<!DOCTYPE html>
<html lang="en">
<head>
<meta charset="utf-8">
<title>Harbor Youth Retreat – Partner Presentation</title>
<link rel="stylesheet" href="https://fonts.googleapis.com/css2?family=Sniglet:wght@400;800&family=Questrial&family=Noto+Naskh+Arabic:wght@400;600&display=swap">
<style>
:root{
  --page:#e9e6e1;
  --sky-deep:#17439f;
  --sky-mid:#2f78d3;
  --sky-light:#8cc7f2;
  --palm:#2f8a2c;
  --sand:#efe3bf;
  --sea:#39b4e0;
  --sea-deep:#1a7fc0;
  --card:#ffffff;
  --ink:#1d2a44;
  --title-blue:#3f86d6;
  --accent-orange:#f0662a;
  --accent-red:#e2322a;
  --photo:#b9a48a;
}
*{margin:0;padding:0;box-sizing:border-box}
html,body{width:1200px;height:848px;overflow:hidden;background:var(--page)}
body{position:relative;font-family:"Questrial",Arial,sans-serif;color:var(--ink)}
.spread{position:absolute;display:flex;gap:4px}
.spread--front{left:60px;top:30px}
.spread--back{left:700px;top:30px}
.spread--inside-a{left:60px;top:440px}
.spread--inside-b{left:640px;top:440px}
.panel{position:relative;width:250px;height:370px;overflow:hidden}
.panel__scene{position:absolute;inset:0;
  background:linear-gradient(to bottom,var(--sky-deep) 0%,var(--sky-mid) 35%,var(--sky-light) 70%,var(--palm) 74%,var(--palm) 82%,var(--sand) 82%,var(--sand) 87%,var(--sea) 87%,var(--sea-deep) 100%)}
.panel__header{position:absolute;top:16px;left:0;right:0;text-align:center;color:#fff;font-size:9px;font-weight:400;letter-spacing:.3px}
.panel__header .ar{display:block;font-family:"Noto Naskh Arabic",serif;font-size:8px;margin-top:1px}
.card{position:absolute;left:32px;top:62px;width:186px;height:218px;background:var(--card);padding:12px;font-size:6.3px;line-height:1.35;overflow:hidden}
.card__title{color:var(--accent-orange);font-size:9px;font-weight:400;text-align:center;line-height:1.15;margin-bottom:6px}
.card__lede{color:var(--title-blue);font-size:8px;text-align:center;line-height:1.15;margin-bottom:4px}
.card p{margin-bottom:5px}
.card--centered p{text-align:center}
.cols{display:flex;gap:8px}
.cols ul{list-style:none;flex:1}
.cols li{margin-bottom:3px}
.ar-text{font-family:"Noto Naskh Arabic",serif;direction:rtl;text-align:right;font-size:7px;line-height:1.5}
.ar-text li{list-style:none;margin-bottom:2px}
.note{color:var(--accent-red)}
.photo{position:absolute;background:var(--photo);border:2px solid #fff;box-shadow:0 1px 2px rgba(0,0,0,.3)}
.badge{position:absolute;width:24px;height:18px;border-radius:4px;background:var(--sky-deep)}
.cover .card{text-align:center;padding-top:30px}
.cover__name{font-family:"Sniglet",sans-serif;font-weight:800;color:var(--title-blue);font-size:25px;line-height:1.15}
.cover__tag{margin-top:22px;color:var(--accent-orange);font-size:12px}
.cover__sub{margin-top:8px;font-size:7px}
</style>
</head>
<body>

<section class="spread spread--front">
  <article class="panel">
    <div class="panel__scene" role="img" aria-label="Blue sky with clouds, hot-air balloon, palm trees and beach"></div>
    <h2 class="panel__header">PRE-COLLEGE &amp; BEYOND</h2>
    <div class="card">
      <h3 class="card__title">The widest range of<br>pre-college Programs</h3>
      <div class="cols">
        <ul>
          <li>One retreat, many revenue streams: summer programs that parents book again every year.</li>
          <li>- Internships</li>
          <li>- Specialties: archaeology, culinary arts, etc.</li>
          <li>- Visual &amp; performing arts</li>
          <li>- Fitness and weight management</li>
          <li>- Special needs "Combination summer"</li>
          <li>- Gifted programs</li>
        </ul>
        <ul>
          <li>- Academic programs on college campuses</li>
          <li>- Language learning and cultural immersion</li>
          <li>- College prep, SAT &amp; ESL programs</li>
          <li>- Community service</li>
          <li>- Adventure expeditions</li>
          <li>- Leadership programs</li>
          <li>- Teen travel</li>
          <li>- Sports</li>
        </ul>
      </div>
    </div>
  </article>
  <article class="panel cover">
    <div class="panel__scene" role="img" aria-label="Blue sky with sun rays, clouds, seagull, hot-air balloon, palm trees and beach"></div>
    <div class="card">
      <h1 class="cover__name">Harbor<br>Youth<br>Retreat</h1>
      <p class="cover__tag">Get Ready for Fun</p>
      <p class="cover__sub">Partnership presentation for investors</p>
    </div>
  </article>
</section>

<section class="spread spread--back">
  <article class="panel">
    <div class="panel__scene" role="img" aria-label="Blue sky with clouds, hot-air balloon, palm trees and beach"></div>
    <h2 class="panel__header">Kids Going to Summer Camp<span class="ar">أطفال يذهبون إلى المخيم الصيفي</span></h2>
    <div class="card card--centered">
      <h3 class="card__title">Why You Want to<br>Work with us</h3>
      <p>We know the families and the market. Our customized advisory process matches each child to the right program, builds trust with parents and turns first-time bookings into yearly returns.</p>
      <p>A clear model: small advisory fees, program partnerships and our own retreat sessions. Partner with us to establish the company and share in its growth.</p>
    </div>
  </article>
</section>

<section class="spread spread--inside-a">
  <article class="panel">
    <div class="panel__scene" role="img" aria-label="Blue sky with clouds, seagull, palm trees and beach"></div>
    <h2 class="panel__header"><span class="ar">أطفال يذهبون إلى المخيم الصيفي هذا العام</span></h2>
    <div class="card">
      <ul class="ar-text">
        <li>برامج رياضية وفنية متنوعة</li>
        <li>مخيمات تعليمية للمراهقين</li>
        <li>رحلات مغامرة وخدمة المجتمع</li>
        <li>برامج القيادة والتطوع</li>
        <li>تعلم اللغات والثقافات</li>
        <li>مخيمات الحاسوب والتصميم</li>
        <li>برامج خاصة للموهوبين</li>
        <li class="note">شراكة للنمو في سوق المخيمات الصيفية</li>
      </ul>
    </div>
    <div class="badge" style="left:4px;top:130px"></div>
    <div class="badge" style="left:4px;top:170px"></div>
  </article>
  <article class="panel">
    <div class="panel__scene" role="img" aria-label="Blue sky with clouds, hot-air balloon, palm trees and beach"></div>
    <div class="card">
      <div class="cols">
        <ul>
          <li class="card__lede">Kids Going to Summer Camp</li>
          <li>Finding the right summer camp is where it all begins. Every happy camper brings a family back next year.</li>
          <li>- Single-gender, co-ed &amp; brother-sister camps<br>- Traditional summer camps<br>- Sports camps<br>- First-time campers<br>- Specialty camps<br>- Gifted programs<br>- Teen &amp; tween camps</li>
        </ul>
        <ul>
          <li class="card__lede">Pre-College &amp; Beyond</li>
          <li>The years before college are a growing market as families invest in admissions success.</li>
          <li>- Academic enrichment<br>- Language learning<br>- Visual and performing arts<br>- Community service<br>- Leadership training<br>- Teen travel<br>- College prep, SAT, ESL</li>
        </ul>
      </div>
    </div>
    <div class="photo" role="img" aria-label="Photo of campers together" style="left:4px;top:120px;width:26px;height:22px"></div>
    <div class="photo" role="img" aria-label="Photo of camp activity" style="left:4px;top:170px;width:26px;height:22px"></div>
    <div class="photo" role="img" aria-label="Photo of students outdoors" style="left:221px;top:110px;width:26px;height:22px"></div>
  </article>
</section>

<section class="spread spread--inside-b">
  <article class="panel">
    <div class="panel__scene" role="img" aria-label="Blue sky with clouds, seagull, hot-air balloon, palm trees and beach"></div>
    <h2 class="panel__header">Kids Going to Summer Camp<span class="ar">أطفال يذهبون إلى المخيم</span></h2>
    <div class="card">
      <p>Summer camp is a major financial and emotional investment for every family – a steady demand our retreat is built to serve.</p>
      <p class="ar-text">المخيم الصيفي استثمار مهم في نمو الطفل وذكرى تدوم مدى الحياة</p>
      <ul class="ar-text">
        <li>مخيمات قصيرة المدة</li>
        <li>مخيمات للأطفال ذوي الحساسية</li>
        <li>مخيمات رياضية</li>
        <li>مخيمات أكاديمية</li>
        <li>برامج الموهوبين</li>
      </ul>
    </div>
    <div class="photo" role="img" aria-label="Photo of campers" style="left:4px;top:110px;width:26px;height:22px"></div>
    <div class="photo" role="img" aria-label="Photo of a camp group" style="left:4px;top:190px;width:26px;height:22px"></div>
    <div class="photo" role="img" aria-label="Photo of children at camp" style="left:221px;top:220px;width:26px;height:22px"></div>
  </article>
  <article class="panel">
    <div class="panel__scene" role="img" aria-label="Blue sky with clouds, hot-air balloon, palm trees and beach"></div>
    <h2 class="panel__header">Kids Going to Summer Camp<span class="ar">أطفال يذهبون إلى المخيم الصيفي</span></h2>
    <div class="card">
      <div class="cols">
        <ul>
          <li>There are thousands of camps! Our process lets us serve every segment of the market.</li>
          <li>- Shorter sessions</li>
          <li>- Camps for kids with food allergies</li>
          <li>- Strong staff training</li>
          <li>- Sports Camps</li>
          <li>- Academic Camps</li>
          <li>- Computer, game &amp; web design camp</li>
          <li>- Gifted programs</li>
          <li>- Teen camps</li>
        </ul>
        <ul>
          <li>- Co-ed camps</li>
          <li>- Single-gender camps</li>
          <li>- Brother-sister camps</li>
          <li>- Special needs and performing arts camps</li>
          <li>- Weight management programs</li>
          <li>- Special focus camps: cooking, horseback riding etc.</li>
          <li class="note">Join us as a partner and help us open the first Harbor Youth Retreat season.</li>
        </ul>
      </div>
    </div>
  </article>
</section>

</body>
</html>
```